依頼詳細
新しく名刺を作ります。ARでスマホ等でスキャンすると動画が流せる企画物の名刺です。
ARでスキャンするマーカにする為にいくつか制約があります。以下の物使用しないで下さい。
グラデーションの物 (文字・背景にグラデーションがある物)
パターン柄の物 (水玉模様・唐草模様)
背景と文字・オブジェクトの色の境目が曖昧な物 (スキャンする際モノクロで判断するため、境目がはっきりしない物)
記載項目
Calventrix
代表取締役
三津谷 和臣 Kazuomi Mitsuya
mitsuya@calventrix-mail.jp
090-5172-3948
株式会社カルヴェントリクス
本社 〒358-0275
栃木県足利市芳野町947-6
Tel 0284-67-3152
Fax 0284-67-3150
工場 栃木県足利市芳野町1584-9
希望イメージ
シンプル 複雑
単色 カラフル
暗い 明るい
日常 高級
遊び心 厳粛
未来的 伝統的
女性的 男性的
希望する色
緑系、黄・オレンジ系
納品ファイル
• イラストレーター形式 (.ai)
当選作品は内容の修正・変更をする場合があります。

```html
<!DOCTYPE html>
<html lang="ja">
<head>
<meta charset="utf-8">
<title>Calventrix 名刺</title>
<link href="https://fonts.googleapis.com/css2?family=Noto+Sans+JP:wght@400;500;700&display=swap" rel="stylesheet">
<style>
  :root{
    --brand-green:#2f9a3f;
    --paper:#ffffff;
    --ink:#333333;
    --ground:#eceeec;
  }
  html,body{margin:0;padding:0;}
  body{
    width:1200px;height:2508px;overflow:hidden;
    background:var(--ground);
    font-family:"Noto Sans JP",sans-serif;
    color:var(--ink);
    position:relative;
  }
  .card{
    position:absolute;left:100px;width:1000px;height:604px;
    overflow:hidden;box-shadow:0 6px 24px rgba(0,0,0,.12);
  }
  .card--front{top:520px;background:var(--brand-green);}
  .card--back{top:1380px;background:var(--paper);}
  .company-name{
    position:absolute;margin:0;
    font-family:"Noto Sans JP",sans-serif;font-weight:700;
    line-height:1;white-space:nowrap;
  }
  .card--front .company-name{left:70px;top:250px;font-size:86px;color:var(--paper);}
  .card--back .company-name{left:300px;top:62px;font-size:72px;color:var(--brand-green);}
  .company{position:absolute;left:304px;top:166px;font-size:24px;font-weight:700;color:var(--brand-green);margin:0;}
  .address{position:absolute;left:304px;top:206px;font-size:17px;line-height:1.6;margin:0;}
  .person{position:absolute;left:304px;top:360px;}
  .person .title{font-size:19px;margin:0 0 6px;}
  .person .name{font-size:52px;font-weight:500;margin:0;letter-spacing:6px;line-height:1.15;}
  .person .romaji{font-size:18px;margin:6px 0 0;}
  .contact{position:absolute;right:48px;bottom:54px;font-size:18px;line-height:1.7;margin:0;}
  .icon{display:inline-block;width:18px;height:18px;vertical-align:-3px;margin-right:8px;}
</style>
</head>
<body>
  <section class="card card--front" aria-label="名刺 表面">
    <p class="company-name">Calventrix</p>
  </section>

  <section class="card card--back" aria-label="名刺 裏面">
    <p class="company-name">Calventrix</p>
    <p class="company">株式会社カルヴェントリクス</p>
    <p class="address">
      本社 〒358-0275 栃木県足利市芳野町947-6<br>
      Tel 0284-67-3152　Fax 0284-67-3150<br>
      工場 栃木県足利市芳野町1584-9
    </p>
    <div class="person">
      <p class="title">代表取締役</p>
      <p class="name">三津谷 和臣</p>
      <p class="romaji">Kazuomi Mitsuya</p>
    </div>
    <p class="contact">
      <svg class="icon" viewBox="0 0 24 24"><path fill="#2f9a3f" d="M6.6 10.8a15.1 15.1 0 0 0 6.6 6.6l2.2-2.2c.3-.3.7-.4 1-.2 1.1.4 2.3.6 3.6.6.6 0 1 .4 1 1V20c0 .6-.4 1-1 1A17 17 0 0 1 3 4c0-.6.4-1 1-1h3.5c.6 0 1 .4 1 1 0 1.3.2 2.5.6 3.6.1.3 0 .7-.2 1z"/></svg>090-5172-3948<br>
      <svg class="icon" viewBox="0 0 24 24"><rect x="2" y="5" width="20" height="14" rx="2" fill="#2f9a3f"/><path d="M3 6l9 7 9-7" stroke="#fff" stroke-width="2" fill="none"/></svg>mitsuya@calventrix-mail.jp
    </p>
  </section>
</body>
</html>
```